Meridane Works, Inc. - Update our Website

Meridane Works needs a website to help our customers to navigate through our services efficiently. Our existing website is at www.meridwork.example

We would like to explain our services with content and pictures (photographs) that distinguishes our products and services from our competition.

The website design must implement a strategy to focus on our Contract Labeling services.

With this new design we would like to attract new customers and ensure that our existing customers are fully informed with our latest offerings.

```html
<!DOCTYPE html>
<html lang="en">
<head>
<meta charset="utf-8">
<title>Meridane Works, Inc.</title>
<link href="https://fonts.googleapis.com/css2?family=Open+Sans:wdth,wght@75..100,400..700&display=swap" rel="stylesheet">
<style>
:root{
  --bg:#efe8d6;
  --page:#ffffff;
  --blue:#0f6fa8;
  --blue-dark:#0b5a8c;
  --orange:#f57c00;
  --orange-dark:#d9620a;
  --text:#555555;
  --nav:#222222;
  --footer:#3b3b3d;
}
*{margin:0;padding:0;box-sizing:border-box}
html,body{width:882px;height:1200px;overflow:hidden}
body{background:var(--bg);font-family:"Open Sans",sans-serif;color:var(--text);position:relative}
.page{position:absolute;left:118px;top:0;width:646px;height:1200px;background:var(--page);box-shadow:0 0 6px rgba(0,0,0,.15)}
.top{position:absolute;left:0;top:0;width:646px;height:62px;background:linear-gradient(#e2e2e2,#d6d6d6)}
.brand{position:absolute;left:0;top:18px;width:646px;display:flex;justify-content:center;align-items:center;gap:6px}
.brand-dot{width:24px;height:24px;border-radius:50%;background:var(--orange)}
.brand-name{font-size:11px;font-weight:700;color:#2b2b2b;letter-spacing:.5px}
.nav{position:absolute;left:0;top:62px;width:646px;height:49px;background:#fff;display:flex;align-items:center;padding-left:61px;font-size:8.5px;font-weight:600;color:var(--nav)}
.nav a{text-decoration:none;color:inherit;margin-right:36px}
.nav a.active{background:var(--orange);color:#fff;padding:7px 14px}
.band{position:absolute;left:0;top:111px;width:646px;height:213px;background:linear-gradient(#d0d0d0,#e4e4e4);border-bottom:1px solid #c8c8c8}
.slider{position:absolute;left:14px;top:130px;width:618px;height:268px;background:#fff;border:1px solid #cfcfcf;box-shadow:0 4px 8px rgba(0,0,0,.15)}
.slide{position:absolute;left:7px;top:6px;width:604px;height:254px;background:linear-gradient(100deg,#6b6f78 0%,#9fb4c8 30%,#8ed2f3 55%,#d8f1fc 100%)}
.dots{position:absolute;left:270px;top:236px;width:59px;height:20px;background:#fff;display:flex;justify-content:center;align-items:center;gap:11px}
.dots span{width:6px;height:6px;border-radius:50%;background:var(--blue)}
.dots span.on{background:var(--orange)}
.welcome{position:absolute;left:0;top:425px;width:646px;text-align:center;font-size:16px;color:var(--blue);font-weight:400}
.intro{position:absolute;left:40px;top:449px;width:566px;text-align:center;font-size:8px;line-height:15px;color:#444}
.section-title{position:absolute;left:14px;font-size:15.5px;color:var(--blue);font-weight:400}
.card{position:absolute;width:196px}
.card-head{height:37px;background:linear-gradient(var(--blue),var(--blue-dark));color:#fff;font-size:11px;font-weight:600;font-stretch:92%;white-space:nowrap;overflow:hidden;padding:12px 8px 0 10px;letter-spacing:-.1px}
.card-img{height:119px}
.card-text{margin-top:13px;font-size:8.6px;line-height:15px;color:var(--text);height:64px}
.more{display:block;height:38px;background:linear-gradient(var(--orange),var(--orange-dark));color:#fff;text-align:center;font-size:11.5px;font-weight:600;line-height:38px;text-decoration:none}
.feature{position:absolute;left:436px;top:838px;width:196px;height:282px;background:linear-gradient(#1877b2,#0c5d92);color:#fff;text-align:center}
.feature h3{font-size:11.5px;font-weight:600;margin-top:20px}
.feature-img{position:absolute;left:17px;top:47px;width:163px;height:89px;background:linear-gradient(#fff,#e6eef4);border:1px solid #fff}
.feature p{position:absolute;left:14px;top:147px;width:168px;font-size:8.3px;font-weight:600;line-height:15px}
.feature .more{position:absolute;left:33px;top:216px;width:130px}
.footer{position:absolute;left:0;top:1152px;width:646px;height:48px;background:var(--footer);color:#bbb;font-size:8px}
.copy{position:absolute;left:13px;top:21px}
.social{position:absolute;right:22px;top:19px;display:flex;gap:10px}
.social span{width:12px;height:12px;border-radius:50%;background:#9a9a9a}
</style>
</head>
<body>
<div class="page">
  <header class="top">
    <div class="brand"><span class="brand-dot"></span><span class="brand-name">MERIDANE WORKS INC.</span></div>
  </header>
  <nav class="nav">
    <a class="active" href="#">HOME</a><a href="#">ABOUT US</a><a href="#">SERVICES</a><a href="#">PRODUCTS</a><a href="#">PROJECTS</a><a href="#">BLOG</a><a href="#">CONTACT US</a>
  </nav>
  <div class="band"></div>
  <div class="slider">
    <div class="slide" role="img" aria-label="Businessman touching a glowing virtual keyboard and keypad"></div>
    <div class="dots"><span></span><span class="on"></span><span></span></div>
  </div>

  <h1 class="welcome">WELCOME TO MERIDANE WORKS, INC.</h1>
  <p class="intro">Meridane Works, Inc. specializes in providing products and services to the pharmaceutical industry. We are focused on the needs of those individuals involved with Clinical Trial Materials.</p>

  <h2 class="section-title" style="top:489px">SERVICES</h2>
  <div class="card" style="left:15px;top:521px">
    <div class="card-head">MeriServ™</div>
    <div class="card-img" role="img" aria-label="Hands reviewing charts on a tablet beside a coffee cup" style="background:linear-gradient(135deg,#e9ecef,#c9d4dc)"></div>
    <p class="card-text">MeriServ™ is a contract clinical label generation service that provides you with ready to apply clinical labels specifically designed and produced for your clinical...</p>
    <a class="more" href="#">MORE</a>
  </div>
  <div class="card" style="left:225px;top:521px">
    <div class="card-head">MeriBook™-Clinical Booklet Labels</div>
    <div class="card-img" role="img" aria-label="Close-up of program code on a blue screen" style="background:linear-gradient(160deg,#0a2f8a,#2f7fe0 60%,#0b3aa0)"></div>
    <p class="card-text">MeriBook™ labels are multi-page clinical labels used to address the needs of multi-language studies. This enables user to prepare and ship clinical materials to multiple...</p>
    <a class="more" href="#">MORE</a>
  </div>
  <div class="card" style="left:436px;top:521px">
    <div class="card-head">Clinical Randomizations</div>
    <div class="card-img" role="img" aria-label="Laptop on a globe against a blue data background" style="background:linear-gradient(135deg,#0d6fb0,#7fd0f0 55%,#1a86c4)"></div>
    <p class="card-text">Our systems can create randomization data for all types of CTM requirements. Patient randomization, material randomization and random...</p>
    <a class="more" href="#">MORE</a>
  </div>

  <h2 class="section-title" style="top:816px">SOFTWARE PRODUCTS</h2>
  <div class="card" style="left:15px;top:849px">
    <div class="card-head">MeriPro/LBL™</div>
    <div class="card-img" role="img" aria-label="Digital data tunnel with rows of computer screens" style="background:linear-gradient(#081a5c,#1d5fd0 55%,#050f3a)"></div>
    <p class="card-text">MeriPro/LBL™ is the industry's leading clinical label generation system offering superior overall capability and flexibility The system enables users to...</p>
    <a class="more" href="#">MORE</a>
  </div>
  <div class="card" style="left:225px;top:849px">
    <div class="card-head">Software Validation Services</div>
    <div class="card-img" role="img" aria-label="Hand selecting figures in a people network diagram" style="background:radial-gradient(circle at 55% 45%,#e8e8e8,#6d6d6d 75%)"></div>
    <p class="card-text">Meridane Works offers software validation services for the FDA regulated industry. Our knowledge of industry practices and standards...</p>
    <a class="more" href="#">MORE</a>
  </div>
  <div class="feature">
    <h3>Clinical Label Stock</h3>
    <div class="feature-img" role="img" aria-label="Globe connected to surrounding laptops"></div>
    <p>MeriStock™ is a premium line of label products that we supply to the pharmaceutical industry. These label stocks are specifically designed...</p>
    <a class="more" href="#">MORE</a>
  </div>

  <footer class="footer">
    <p class="copy">:: © 2014 Meridane Works, Inc. All rights reserved. &nbsp;::</p>
    <div class="social" aria-label="Social links"><span></span><span></span><span></span><span></span><span></span></div>
  </footer>
</div>
</body>
</html>
```